Cover art for debut single - band name lantern of tide

Create a music release cover. The cover will be a single release (side A and B) but will only be released on digital streaming and download platforms. We have an existing image that needs to be part of the design, what is required to augment this existing image, is a logo and text for the title of the song being released. The song title is "Harbor"

Target Market(s)

Any age group of music listener but likely someone who was in their teens or twenties in the 90s.

Industry/Entity Type

Music Download

Logo Text

Lantern of Tide or LoT

Font styles to use
Sans Serif
Other font styles liked:
• I like Sans Serif as basis of the font generally but I am also keen to see what can be done with "Brisk Gleam" https://typeshelfarchive.example/faces/58214/brisk-gleam

Colors

Designer to choose colors to be used in the design.

Requirements
Must have
• I must have the image provided featured in the cover art, the logo you will design and the text for the title of the song being released.
• My initial idea was for a completely white cover with the provided image centred. The logo place perhaps in one corner and the title of the track in another corner. The song's title is "Harbor" and should be textually represented on the cover.
• The finished product for the single's cover must include jpg files that are 3000 x 3000 pixels square and the follow variations:
• 4000 x 4000
• 5000 x 5000
• 6000 x 6000
• We will also need the bands name logo separately as well. To be clear the band name is Lantern of Tide but we are equally interested in the logo using the acronym LoT.

```html
<!DOCTYPE html>
<html lang="en">
<head>
<meta charset="utf-8">
<title>Lantern of Tide — Harbor</title>
<link rel="stylesheet" href="https://fonts.googleapis.com/css2?family=Antonio:wght@100&family=Mrs+Saint+Delafield&display=swap">
<style>
  :root {
    --backdrop: #e3e3e3;
    --paper: #ffffff;
    --ink: #231f20;
    --art-light-a: #f1f1f1;
    --art-light-b: #e2e2e2;
    --art-dark-a: #2f2b2c;
    --art-dark-b: #464243;
  }
  html, body {
    margin: 0;
    padding: 0;
    overflow: hidden;
  }
  body {
    width: 1200px;
    height: 1200px;
    background: var(--backdrop);
    position: relative;
  }
  .cover {
    position: absolute;
    left: 350px;
    width: 500px;
    height: 500px;
    box-sizing: border-box;
  }
  .cover--light { top: 72px; background: var(--paper); color: var(--ink); }
  .cover--dark { top: 619px; background: var(--ink); color: var(--paper); }

  .band-name {
    position: absolute;
    top: 38px;
    left: 0;
    right: 10px;
    margin: 0;
    text-align: center;
    font-family: "Mrs Saint Delafield", cursive;
    font-weight: 400;
    font-size: 66px;
    line-height: 1;
    white-space: nowrap;
  }
  .artwork {
    position: absolute;
    left: 28px;
    top: 218px;
    width: 446px;
    height: 94px;
  }
  .cover--light .artwork {
    background: linear-gradient(90deg, var(--art-light-a), var(--art-light-b) 50%, var(--art-light-a));
  }
  .cover--dark .artwork {
    background: linear-gradient(90deg, var(--art-dark-a), var(--art-dark-b) 50%, var(--art-dark-a));
  }

  .song-title {
    position: absolute;
    top: 412px;
    left: 0;
    right: 0;
    margin: 0;
    text-align: center;
    font-family: "Antonio", sans-serif;
    font-weight: 100;
    font-size: 38px;
    letter-spacing: 1.05em;
    text-indent: 1.05em;
    line-height: 1;
    text-transform: uppercase;
  }
</style>
</head>
<body>
  <section class="cover cover--light">
    <h1 class="band-name">Lantern of Tide</h1>
    <div class="artwork" role="img" aria-label="Row of seven continuous-line drawn faces in black ink"></div>
    <h2 class="song-title">Harbor</h2>
  </section>

  <section class="cover cover--dark">
    <h1 class="band-name">Lantern of Tide</h1>
    <div class="artwork" role="img" aria-label="Row of seven continuous-line drawn faces in white ink"></div>
    <h2 class="song-title">Harbor</h2>
  </section>
</body>
</html>
```